Mixed Martial Arts gym that is known for high quality athletes, students and training

We need a business card designed that is unique and stands out. Something that is not so dark and boring but looks 'energetic' to those that are given it. The customers that would receive this card would be looking to sign up for martial arts or fitness training and this card is used for corporate sponsorships and networking as well.

Marcus Pellow-Grant
0417305962 or 0409561738
Level 1, 284 Wendover Road. Carrowbrook NSW 2871
marcus@kinetiqcombatworks.com.au
www.kinetiqcombatworks.com

```html
<!DOCTYPE html>
<html lang="en">
<head>
<meta charset="utf-8">
<title>Kinetiq Combat Works – Business Card</title>
<link rel="stylesheet" href="https://fonts.googleapis.com/css2?family=Questrial&display=swap">
<style>
  :root {
    --stage-top: #3f3f3f;
    --stage-bottom: #8a8a8a;
    --card-white: #ffffff;
    --charcoal: #333033;
    --orange: #f7941d;
    --ink: #2d2d2d;
    --muted: #6f6f6f;
    --light-text: #e6e6e6;
  }
  * { margin: 0; padding: 0; box-sizing: border-box; }
  html, body { width: 1200px; height: 1000px; overflow: hidden; }
  body {
    background: linear-gradient(180deg, var(--stage-top), var(--stage-bottom));
    font-family: "Questrial", "Century Gothic", sans-serif;
    position: relative;
  }
  .card {
    position: absolute;
    top: 342px;
    width: 510px;
    height: 315px;
    background: var(--card-white);
    overflow: hidden;
    box-shadow: 0 2px 6px rgba(0,0,0,0.45);
  }
  .card--front { left: 60px; }
  .card--back { left: 630px; }
  .card__art { position: absolute; inset: 0; width: 100%; height: 100%; }

  .identity { position: absolute; left: 267px; top: 28px; }
  .identity__name { font-size: 21px; font-weight: 400; color: var(--ink); letter-spacing: 0.2px; }
  .identity__title { font-size: 14px; color: var(--muted); margin-top: 2px; }

  .contact {
    position: absolute; left: 38px; top: 172px;
    list-style: none; color: var(--light-text); font-size: 14px; line-height: 19px;
  }
  .contact li { display: flex; align-items: center; gap: 6px; }
  .contact svg { width: 11px; height: 11px; flex: none; }

  .brand {
    position: absolute; left: 0; right: 0; top: 100px;
    display: flex; justify-content: center; align-items: center; gap: 10px;
    color: var(--orange); font-size: 30px; letter-spacing: 0.5px;
  }
  .brand__dot { width: 14px; height: 14px; border-radius: 50%; background: var(--orange); }
</style>
</head>
<body>
  <section class="card card--front" aria-label="Business card front">
    <svg class="card__art" viewBox="0 0 510 315" aria-hidden="true">
      <rect x="0" y="140" width="510" height="175" fill="var(--charcoal)"/>
      <polygon points="427,140 510,140 510,315 332,315" fill="var(--orange)"/>
    </svg>
    <div class="identity">
      <h1 class="identity__name">Marcus Pellow-Grant</h1>
      <p class="identity__title">Managing Director</p>
    </div>
    <ul class="contact">
      <li><svg viewBox="0 0 12 12"><path d="M3 1 L5 3.5 L4 5 Q5 7 7 8 L8.5 7 L11 9 L9.5 11 Q4 10.5 1 3 Z" fill="var(--orange)"/></svg>0409561738</li>
      <li><svg viewBox="0 0 12 12"><path d="M3 1 L5 3.5 L4 5 Q5 7 7 8 L8.5 7 L11 9 L9.5 11 Q4 10.5 1 3 Z" fill="var(--orange)"/></svg>0417305962</li>
      <li><svg viewBox="0 0 12 12"><rect x="1" y="2.5" width="10" height="7" fill="none" stroke="var(--orange)" stroke-width="1.3"/><path d="M1 2.5 L6 6.5 L11 2.5" fill="none" stroke="var(--orange)" stroke-width="1.3"/></svg>marcus@kinetiqcombatworks.com.au</li>
      <li><svg viewBox="0 0 12 12"><circle cx="6" cy="6" r="5" fill="none" stroke="var(--orange)" stroke-width="1.2"/><path d="M1 6 H11 M6 1 Q3 6 6 11 M6 1 Q9 6 6 11" fill="none" stroke="var(--orange)" stroke-width="1"/></svg>www.kinetiqcombatworks.com</li>
      <li>Level 1, 284 Wendover Road.</li>
      <li>Carrowbrook NSW 2871</li>
    </ul>
  </section>

  <section class="card card--back" aria-label="Business card back">
    <svg class="card__art" viewBox="0 0 510 315" aria-hidden="true">
      <rect x="0" y="252" width="510" height="63" fill="var(--charcoal)"/>
      <polygon points="390,252 510,252 510,315 333,315" fill="var(--orange)"/>
    </svg>
    <div class="brand">
      <span class="brand__dot"></span>
      <span class="brand__name">Kinetiq Combat Works</span>
    </div>
  </section>
</body>
</html>
```